Generic Post Card

New Product promotion. Attached is a card we did earlier. I made modifications to it so you can get an idea of what I want. The colors match our web page at quorvelmist.com

Product

```html
<!DOCTYPE html>
<html lang="en">
<head>
<meta charset="utf-8">
<title>Nitrous Oxide Inhaler – Postcard</title>
<link rel="stylesheet" href="https://fonts.googleapis.com/css2?family=Roboto+Condensed:wght@700&family=Lato:wght@400;700;900&family=Exo+2:wght@600&display=swap">
<style>
  :root {
    --navy: #1f3f7a;
    --blue: #2d5a9a;
    --blue-light: #4b78b4;
    --orange: #f7a21b;
    --orange-deep: #ef8a12;
    --ink: #111111;
    --paper: #ffffff;
    --mist: #eceded;
    --stage: #e6e7e9;
    --line: #2b2b2b;
    --skin: #cfa58c;
    --skin-light: #ecd9cb;
    --sage: #86ab9d;
  }
  * { box-sizing: border-box; margin: 0; padding: 0; }
  html, body { width: 900px; height: 1200px; overflow: hidden; }
  body { background: var(--stage); font-family: "Lato", sans-serif; position: relative; }

  .card { position: absolute; background: var(--paper); box-shadow: 0 4px 14px rgba(0,0,0,.18); overflow: hidden; }

  /* ---------- Front ---------- */
  .front { left: 148px; top: 78px; width: 605px; height: 468px;
    background: linear-gradient(#fff 0%, var(--mist) 100%); }
  .front-title { height: 56px; background: linear-gradient(var(--blue-light), var(--navy));
    font-family: "Roboto Condensed", sans-serif; font-weight: 700; font-size: 37px;
    color: var(--paper); text-align: center; line-height: 62px; }
  .front-title .accent { color: var(--orange); }
  .front-tagline { height: 50px; border-top: 2px solid var(--orange); border-bottom: 2px solid var(--orange);
    background: linear-gradient(#fff, #eeeeee);
    font-weight: 900; font-size: 25px; color: var(--ink); text-align: center; line-height: 44px; }
  .front-tagline .key { color: var(--navy); }

  .steps { position: absolute; top: 131px; left: 0; width: 100%; }
  .step { position: absolute; width: 140px; text-align: center; }
  .step:nth-child(1) { left: 33px; }
  .step:nth-child(2) { left: 234px; }
  .step:nth-child(3) { left: 434px; }
  .step-photo { width: 140px; height: 140px; border-radius: 50%; border: 4px solid var(--orange);
    box-shadow: 0 6px 8px rgba(0,0,0,.15); }
  .photo-device { background: radial-gradient(circle at 58% 50%, #ffffff 0%, #f1f2f3 45%, #d6d9dc 100%); }
  .photo-use { background: radial-gradient(circle at 35% 55%, var(--skin-light) 0%, var(--skin) 55%, #b9b9b6 100%); }
  .photo-patient { background: radial-gradient(circle at 50% 32%, var(--skin-light) 0%, var(--skin) 40%, var(--sage) 100%); }
  .step-label { display: inline-block; margin-top: 22px; width: 110px; height: 25px; border: 1.5px solid var(--navy);
    border-radius: 13px; font-size: 10px; font-weight: 700; line-height: 22px; color: var(--ink); background: #fff; }
  .step-label.italic { font-style: italic; }

  .front-footer { position: absolute; left: 0; bottom: 0; width: 100%; height: 96px;
    background: linear-gradient(var(--blue-light), var(--navy)); }
  .nurse-banner { position: absolute; left: 118px; top: 347px; width: 366px; height: 44px;
    background: linear-gradient(var(--orange), var(--orange-deep)); font-weight: 700; font-size: 15px;
    color: var(--ink); text-align: center; line-height: 44px; }
  .nurse-banner::before, .nurse-banner::after { content: ""; position: absolute; bottom: -17px; border-style: solid; }
  .nurse-banner::before { left: -18px; border-width: 0 18px 17px 0; border-color: transparent #b96a08 transparent transparent; }
  .nurse-banner::after { right: -18px; border-width: 0 0 17px 18px; border-color: transparent transparent transparent #b96a08; }
  .contact { position: absolute; top: 38px; height: 30px; color: var(--paper); display: flex; align-items: center; gap: 6px; }
  .contact.phone { left: 33px; font-family: "Roboto Condensed", sans-serif; font-size: 25px; font-weight: 700; }
  .contact.web { right: 53px; font-weight: 700; font-size: 17px; }
  .divider { position: absolute; left: 284px; top: 40px; width: 1px; height: 26px; background: rgba(255,255,255,.8); }

  /* ---------- Back ---------- */
  .back { left: 145px; top: 637px; width: 610px; height: 473px; }
  .back-art { position: absolute; left: 0; top: 0; width: 295px; height: 390px;
    background: linear-gradient(#ffffff, #f0f0f0); }
  .back-header { height: 88px; background: linear-gradient(var(--navy), var(--blue-light));
    color: var(--paper); text-align: center; padding-top: 20px; }
  .back-header .small { font-size: 13px; }
  .back-header .big { font-size: 17px; line-height: 21px; }
  .back-device { position: absolute; left: 150px; top: 100px; width: 56px; height: 150px;
    background: linear-gradient(90deg, #d9dcdf, #ffffff 45%, #e3e5e7); border-radius: 14px 14px 22px 22px;
    box-shadow: 0 3px 6px rgba(0,0,0,.12); }
  .qualities { position: absolute; left: 34px; top: 136px; font-family: "Exo 2", sans-serif;
    font-weight: 600; font-size: 23px; line-height: 28px; color: var(--ink); list-style: none; }
  .qualities li { width: 50px; border-bottom: 1.5px solid var(--orange); padding-bottom: 4px; margin-bottom: 3px; white-space: nowrap; }
  .qualities li:last-child { border-bottom: 0; }
  .back-patient { position: absolute; left: 190px; top: 188px; width: 105px; height: 143px;
    background: radial-gradient(ellipse at 50% 25%, var(--skin-light) 0%, var(--skin) 35%, var(--sage) 80%);
    border-radius: 50% 50% 0 0 / 30% 30% 0 0; }
  .back-phone { position: absolute; left: 30px; top: 288px; font-size: 19px; font-weight: 700;
    color: var(--navy); display: flex; align-items: center; gap: 5px; }
  .web-bar { position: absolute; left: 0; top: 331px; width: 303px; height: 58px;
    background: linear-gradient(var(--orange), var(--orange-deep)); font-weight: 700; font-size: 16px;
    color: var(--ink); display: flex; align-items: center; gap: 6px; padding-left: 26px; }
  .stamp-box { position: absolute; left: 501px; top: 48px; width: 68px; height: 68px; border: 1.5px solid var(--line); }
  .address-line { position: absolute; height: 1.5px; background: var(--line); }
</style>
</head>
<body>

<section class="card front" aria-label="Postcard front">
  <h1 class="front-title"><span class="accent">Nitrous Oxide</span> Inhaler</h1>
  <p class="front-tagline">Reduced <span class="key">PAIN</span> and <span class="key">ANXIETY</span> in seconds</p>

  <div class="steps">
    <figure class="step">
      <div class="step-photo photo-device" role="img" aria-label="Photo of the hand-held nitrous oxide inhaler"></div>
      <figcaption class="step-label">Nitrous Oxide Inhaler</figcaption>
    </figure>
    <figure class="step">
      <div class="step-photo photo-use" role="img" aria-label="Photo of a patient using the inhaler"></div>
      <figcaption class="step-label italic">Your painful Procedure</figcaption>
    </figure>
    <figure class="step">
      <div class="step-photo photo-patient" role="img" aria-label="Photo of a smiling patient"></div>
      <figcaption class="step-label italic">Happy Patient</figcaption>
    </figure>
  </div>

  <div class="front-footer">
    <div class="contact phone">
      <svg width="16" height="16" viewBox="0 0 16 16" aria-hidden="true"><rect width="16" height="16" rx="3" fill="#fff"/><path d="M5 3.5c-.8.4-1.4 1-1.4 1.8 0 3.3 3.8 7.2 7.1 7.2.8 0 1.5-.6 1.8-1.4l-2-1.5-1.1.9c-1.3-.6-2.4-1.7-3-3l.9-1.1z" fill="#1f3f7a"/></svg>
      346-555-0148
    </div>
    <span class="divider"></span>
    <div class="contact web">
      <svg width="15" height="15" viewBox="0 0 16 16" aria-hidden="true"><circle cx="8" cy="8" r="7" fill="none" stroke="#fff" stroke-width="1.5"/><path d="M1 8h14M8 1c-3 3-3 11 0 14M8 1c3 3 3 11 0 14" fill="none" stroke="#fff" stroke-width="1.2"/></svg>
      quorvelinhale.com
    </div>
  </div>
  <div class="nurse-banner">Ask your nurse for availability and pricing</div>
</section>

<section class="card back" aria-label="Postcard back">
  <div class="back-art">
    <header class="back-header">
      <p class="small">Hand-held Quorvel: Nitrous Oxide Inhaler</p>
      <p class="big">used to put patients at ease<br>before painful procedures</p>
    </header>
    <div class="back-device" role="img" aria-label="Photo of the hand-held inhaler device"></div>
    <ul class="qualities">
      <li>Soft</li>
      <li>Fast</li>
      <li>Easy</li>
    </ul>
    <div class="back-patient" role="img" aria-label="Photo of a smiling patient with arms crossed"></div>
    <div class="back-phone">
      <svg width="15" height="15" viewBox="0 0 16 16" aria-hidden="true"><rect width="16" height="16" rx="3" fill="#111"/><path d="M5 3.5c-.8.4-1.4 1-1.4 1.8 0 3.3 3.8 7.2 7.1 7.2.8 0 1.5-.6 1.8-1.4l-2-1.5-1.1.9c-1.3-.6-2.4-1.7-3-3l.9-1.1z" fill="#fff"/></svg>
      806-555-0192
    </div>
  </div>
  <div class="web-bar">
    <svg width="15" height="15" viewBox="0 0 16 16" aria-hidden="true"><circle cx="8" cy="8" r="7" fill="none" stroke="#111" stroke-width="1.5"/><path d="M1 8h14M8 1c-3 3-3 11 0 14M8 1c3 3 3 11 0 14" fill="none" stroke="#111" stroke-width="1.2"/></svg>
    www.quorvelmist.com
  </div>

  <div class="stamp-box" aria-label="Stamp area"></div>
  <span class="address-line" style="left:328px;top:236px;width:228px"></span>
  <span class="address-line" style="left:330px;top:266px;width:232px"></span>
  <span class="address-line" style="left:334px;top:288px;width:228px"></span>
</section>

</body>
</html>
```